Virtual Assistant/Online Marketing Business Card/Stationary

I need a professional but modern business card/stationary for my company in Dallas called Brivolo. Brivolo is a virtual assistant specializing in online marketing. I would like a unique design that stands out and makes my brand clear. Incorporating the logo is a must and have attached it to this brief.

Target Market(s)

small business owners & entrepreneurs, 35-65

Industry/Entity Type

Business

Contact Information for Business Card

Maren Tolk
marentolk@brivolo.biz
(555) 271-9064
brivolo.biz

Font styles to use
Sans Serif

Colors
f04a50
3176b5
9bcb3c

Requirements
Must have
• Colors that match the logo colors. Logo integration

```html
<!DOCTYPE html>
<html lang="en">
<head>
<meta charset="utf-8">
<title>Brivolo Stationery</title>
<link rel="stylesheet" href="https://fonts.googleapis.com/css2?family=Source+Sans+3:wght@400;600&display=swap">
<style>
  :root {
    --backdrop: #a9a7a8;
    --paper: #f5f4f2;
    --ink: #2a2a2a;
    --ink-soft: #4a4a4a;
    --dark: #262626;
    --red: #c8402f;
    --envelope-teal: #389ea9;
    --white: #ffffff;
  }
  * { box-sizing: border-box; margin: 0; padding: 0; }
  html, body {
    width: 1200px; height: 811px; overflow: hidden;
    background: var(--backdrop);
    font-family: "Source Sans 3", Arial, sans-serif;
  }
  .canvas { position: relative; width: 1200px; height: 811px; }

  .sheet {
    position: absolute; overflow: hidden;
    background: var(--paper);
    box-shadow: 0 2px 8px rgba(0,0,0,.35);
  }
  .footer-band { position: absolute; left: 0; bottom: 0; width: 100%; background: var(--dark); }
  .footer-band::before {
    content: ""; position: absolute; left: 0; top: 0; width: 100%; height: 4px; background: var(--red);
  }

  .brand-mark {
    position: absolute; display: flex; align-items: center; gap: 7px;
    font-weight: 600; color: var(--ink); line-height: 1;
  }
  .brand-mark .dot { border-radius: 50%; background: var(--red); flex: none; }

  /* Letterhead */
  .letterhead { left: 42px; top: 34px; width: 520px; height: 731px; }
  .letterhead .brand-mark { left: 43px; top: 96px; font-size: 34px; }
  .letterhead .brand-mark .dot { width: 12px; height: 12px; }
  .salutation { position: absolute; left: 43px; top: 204px; font-size: 13.5px; color: var(--ink-soft); }
  .letter-body { position: absolute; left: 43px; top: 247px; width: 440px; }
  .letter-body p { font-size: 7.9px; line-height: 12.5px; color: var(--ink-soft); margin-bottom: 12.5px; text-align: justify; }
  .closing { position: absolute; left: 43px; top: 510px; font-size: 7.8px; color: var(--ink-soft); }
  .signature {
    position: absolute; left: 52px; top: 528px; width: 68px; height: 20px;
    background: linear-gradient(90deg, rgba(30,30,50,.15), rgba(30,30,50,.35), rgba(30,30,50,.1));
    border-radius: 10px;
  }
  .signer { position: absolute; left: 43px; top: 558px; font-size: 16.5px; font-weight: 600; color: var(--ink); }

  .letterhead .footer-band { height: 118px; }
  .contact { position: absolute; right: 30px; top: 649px; text-align: right; color: var(--white); }
  .contact .socials { display: flex; justify-content: flex-end; gap: 2px; margin-bottom: 6px; margin-right: 10px; }
  .contact .socials span { width: 14px; height: 14px; border-radius: 50%; background: var(--white); }
  .contact-line { display: flex; justify-content: flex-end; align-items: center; gap: 7px; font-size: 10.5px; height: 16.4px; }
  .contact-line svg { width: 11px; height: 11px; flex: none; }

  /* Envelope back */
  .envelope-back { left: 580px; top: 204px; width: 582px; height: 262px; background: var(--envelope-teal); }
  .envelope-back .top-band { position: absolute; left: 0; top: 0; width: 100%; height: 112px; background: var(--dark); }
  .envelope-back .top-band::after {
    content: ""; position: absolute; left: 0; bottom: 0; width: 100%; height: 4px; background: var(--red);
  }
  .envelope-back .brand-mark { left: 75px; top: 50px; font-size: 30px; color: var(--white); }
  .envelope-back .brand-mark .dot { width: 10px; height: 10px; background: var(--white); }
  .envelope-back .socials { position: absolute; left: 474px; top: 223px; display: flex; gap: 2px; }
  .envelope-back .socials span { width: 25px; height: 25px; border-radius: 50%; background: var(--white); }

  /* Envelope front */
  .envelope-front { left: 580px; top: 497px; width: 584px; height: 266px; }
  .envelope-front .brand-mark { left: 31px; top: 57px; font-size: 34px; }
  .envelope-front .brand-mark .dot { width: 12px; height: 12px; }
  .envelope-front .footer-band { height: 88px; }
</style>
</head>
<body>
<main class="canvas">

  <section class="sheet letterhead" aria-label="Letterhead">
    <div class="brand-mark"><span class="dot"></span>Brivolo</div>

    <p class="salutation">Dear Mr. Smith,</p>

    <div class="letter-body">
      <p>Thank you for taking the time to speak with our team last week about your plans for the coming season. We were glad to learn more about your shop, your loyal customers and the goals you have set for online growth this year. This letter sums up what we discussed together and the next steps we suggest for your business, so that you can review them at your own pace before we meet again.</p>
      <p>Our assistants can take over your daily inbox, schedule posts across your social channels and keep your customer list tidy and current. Each week you will receive a short report that shows what was done, how your audience responded and which ideas we plan to test next. You stay in control of every decision, and nothing goes out under your name without your approval first.</p>
      <p>We also offer help with email newsletters, simple landing pages and listings on local search sites. Many owners find that a few hours of support each week frees them to focus on sales and service. Our rates are flat and clear, with no long contract, and you may pause or change your plan at any time. We can start small with one channel and add more as results come in, keeping costs steady and easy to track month by month.</p>
      <p>Please look over the attached proposal and let us know if you have any questions. We would be happy to set up a short call to walk through the details and agree on a start date that suits you and your staff.</p>
    </div>

    <p class="closing">Sincerely,</p>
    <div class="signature" role="img" aria-label="Handwritten signature"></div>
    <p class="signer">Maren Tolk</p>

    <div class="footer-band" aria-hidden="true"></div>

    <div class="contact">
      <div class="socials"><span></span><span></span><span></span></div>
      <div class="contact-line">(555) 271-9064
        <svg viewBox="0 0 24 24"><path fill="var(--white)" d="M6.6 10.8a15.2 15.2 0 0 0 6.6 6.6l2.2-2.2c.3-.3.7-.4 1-.2 1.1.4 2.3.6 3.6.6.6 0 1 .4 1 1V20c0 .6-.4 1-1 1A17 17 0 0 1 3 4c0-.6.4-1 1-1h3.5c.6 0 1 .4 1 1 0 1.3.2 2.5.6 3.6.1.3 0 .7-.2 1z"/></svg>
      </div>
      <div class="contact-line">marentolk@brivolo.biz
        <svg viewBox="0 0 24 24"><rect x="2" y="5" width="20" height="14" fill="var(--white)"/><path d="M2 5l10 8 10-8" fill="none" stroke="var(--dark)" stroke-width="1.8"/></svg>
      </div>
      <div class="contact-line">www.brivolo.biz
        <svg viewBox="0 0 24 24"><circle cx="12" cy="12" r="10" fill="var(--white)"/><path d="M2 12h20M12 2c3 3 3 17 0 20M12 2c-3 3-3 17 0 20" fill="none" stroke="var(--dark)" stroke-width="1.5"/></svg>
      </div>
    </div>
  </section>

  <section class="sheet envelope-back" aria-label="Envelope back">
    <div class="top-band" aria-hidden="true"></div>
    <div class="brand-mark"><span class="dot"></span>Brivolo</div>
    <div class="socials"><span></span><span></span><span></span></div>
  </section>

  <section class="sheet envelope-front" aria-label="Envelope front">
    <div class="brand-mark"><span class="dot"></span>Brivolo</div>
    <div class="footer-band" aria-hidden="true"></div>
  </section>

</main>
</body>
</html>
```